Pacific Screen Trade Council is preparing a regular newsletter and needs a design

Our association is made up of media companies, TV stations and video on demand companies. As an association our role is to bring industry together to engage in government dialogues, fight video piracy and hold conferences and events. We are starting a regular newsletter to let our members know what activities we have been undertaking on their behalf and what upcoming activities there are. It will be a combination of text and pictures/ graphics. We have made a lot of changes to the association so we need a design which is professional looking, but also creative and future looking. It should also have a sense of entertainment given it is the video entertainment industry we represent. Attached is an example of a recent newsletter but would like to see something a little more dynamic and professional.

Target Market(s)

Executives in media companies

Font styles to use
Serif

Colors

Designer to choose colors to be used in the design.

Requirements
Must have
• A combination of text, photos and graphics in a modern, personable yet professional layout and design

```html
<!DOCTYPE html>
<html lang="en">
<head>
<meta charset="utf-8">
<title>Newsletter Spread</title>
<link rel="stylesheet" href="https://fonts.googleapis.com/css2?family=Montserrat:wght@400;500;600&display=swap">
<style>
  :root {
    --teal: #0bbfc6;
    --ink-light: #ffffff;
    --ink-dark: #1c2b2f;
    --photo-device-top: #e4e6ea;
    --photo-device-mid: #8d9aa6;
    --photo-device-low: #3b4652;
    --photo-device-base: #1a1a1c;
    --photo-tower-sky: #d9ecf3;
    --photo-tower-mid: #6fa6bd;
    --photo-tower-deep: #1f3b4a;
  }
  * { margin: 0; padding: 0; box-sizing: border-box; }
  html, body { width: 848px; height: 1200px; overflow: hidden; }
  body { font-family: "Montserrat", Arial, sans-serif; background: var(--teal); }
  .page {
    position: relative;
    width: 848px; height: 1200px;
    display: grid;
    grid-template-columns: 424px 424px;
    grid-template-rows: 600px 600px;
  }
  .photo { width: 100%; height: 100%; }
  .photo--device {
    background:
      linear-gradient(180deg, var(--photo-device-top) 0%, #c9ced6 30%, var(--photo-device-mid) 45%, var(--photo-device-low) 68%, #dfe2e6 80%, #a9adb3 86%, var(--photo-device-base) 92%);
  }
  .photo--tower {
    background:
      linear-gradient(165deg, var(--photo-tower-sky) 0%, #b8d8e4 22%, var(--photo-tower-mid) 48%, #2f5566 72%, var(--photo-tower-deep) 100%);
  }
  .panel { position: relative; background: var(--teal); color: var(--ink-light); }
  .section-title {
    position: absolute;
    font-weight: 500;
    font-size: 16px;
    letter-spacing: 0.4px;
    text-transform: uppercase;
    white-space: nowrap;
  }
  .body-copy {
    position: absolute;
    width: 283px;
    font-size: 12.3px;
    line-height: 17.7px;
    text-align: justify;
    hyphens: auto;
  }
  .body-copy p + p { margin-top: 17.7px; }
  .body-copy strong { font-weight: 600; }

  .panel--intro .section-title { left: 69px; top: 83px; }
  .panel--intro .body-copy { left: 69px; top: 126px; }

  .panel--feature .quote-mark {
    position: absolute; left: 72px; top: 684px;
    width: 30px; height: 24px;
  }
  .panel--feature { }
  .pull-quote {
    position: absolute; left: 118px; top: 104px;
    color: var(--ink-dark);
    font-weight: 500;
    font-size: 26.5px;
    line-height: 27px;
    text-transform: uppercase;
    letter-spacing: 0.3px;
  }
  .panel--feature .quote-mark { left: 72px; top: 86px; }
  .panel--feature .section-title { left: 71px; top: 252px; }
  .panel--feature .body-copy { left: 73px; top: 296px; }
</style>
</head>
<body>
<main class="page">
  <div class="photo photo--device" role="img" aria-label="Photo of a tablet showing a video streaming library, with a laptop behind it"></div>

  <section class="panel panel--intro">
    <h2 class="section-title">Voluptatem sequi nesciunt</h2>
    <div class="body-copy">
      <p>Lorem ipsum dolor sit amet, consectetur adipiscing elit, sed do eiusmod tempor incididunt ut labore et dolore magna aliqua. Ut enim ad minim veniam, quis nostrud exercitation ullamco laboris nisi ut aliquip ex ea commodo consequat.</p>
      <p><strong>Duis aute irure dolor in reprehenderit in voluptate velit</strong> esse cillum dolore eu fugiat nulla pariatur. Excepteur sint occaecat cupidatat non proident, sunt in culpa qui officia deserunt mollit anim id est laborum.</p>
      <p>Sed ut perspiciatis unde omnis iste natus error sit voluptatem accusantium doloremque laudantium, <strong>totam rem aperiam,</strong> eaque ipsa quae ab illo inventore veritatis et quasi architecto beatae vitae dicta sunt explicabo. Nemo enim ipsam voluptatem quia voluptas sit aspernatur aut odit aut fugit, sed quia consequuntur magni dolores.</p>
    </div>
  </section>

  <section class="panel panel--feature">
    <svg class="quote-mark" viewBox="0 0 30 24" aria-hidden="true">
      <path fill="#ffffff" d="M0 24V14C0 6 4 1.5 11 0l1.5 3C8.5 4.5 6.5 7 6.3 11H13v13H0zm17 0V14c0-8 4-12.5 11-14l1.5 3c-4 1.5-6 4-6.2 8H30v13H17z"/>
    </svg>
    <blockquote class="pull-quote">Omnis volupta<br>assumenda,<br>est omnislor<br>repellendus</blockquote>
    <h2 class="section-title">Repudiandae et molestiae</h2>
    <div class="body-copy">
      <p>At vero eos et accusamus et iusto odio dignissimos ducimus qui blanditiis praesentium voluptatum deleniti <strong>atque corrupti quos dolores</strong> et quas molestias excepturi sint occaecati cupiditate non provident, similique sunt in culpa qui officia deserunt mollitia animi, id est laborum et dolorum fuga.</p>
      <p>Et harum quidem rerum facilis est et expedita distinctio. Nam libero tempore, cum soluta nobis est eligendi optio cumque nihil impedit quo minus id quod maxime placeat.</p>
    </div>
  </section>

  <div class="photo photo--tower" role="img" aria-label="Upward view of glass office towers against a cloudy sky"></div>
</main>
</body>
</html>
```